Landing Page for a Social Survey

Hi guys,
we need an elegant landing page for a new project. It's a social survey where users need to answer some questions to participate at a lottery.
I attached an example about what we want. As in the example the design should be very elegant and engage to user to click on the button and take part in the survey.
Also the design should look a bit like lumbrook.
If you have any questions, don't hesitate to ask. I'll try to respond as soon as possible.
Please use the following texts:
Header: "Social Network Umfrage"
Headline above the text: "Herzlichen Glückwunsch"
Text:
"Sie wurden als einer von wenigen Nutzern aus Berlin und Umgebung ausgewählt an unserer Umfrage über Social Networks teilzunehmen.
Die Beantwortung der Fragen dauert nur wenige Sekunden. Als Dankeschön für Ihre Teilnahme können Sie ein Zelvo4, Trenu2 oder Pelwin Slate gewinnen."
Button: "Jetzt teilnehmen"

```html
<!DOCTYPE html>
<html lang="de">
<head>
<meta charset="utf-8">
<title>Social Network Umfrage</title>
<link rel="stylesheet" href="https://fonts.googleapis.com/css2?family=Open+Sans:wght@300;400;600&display=swap">
<style>
  :root {
    --brand-blue: #3a5897;
    --brand-blue-dark: #2c4784;
    --text-blue: #3d5a9c;
    --page-top: #ffffff;
    --page-bottom: #d3d8e2;
    --panel-fill: #efefef;
    --panel-edge: #fafafa;
    --white: #ffffff;
    --footer-text: #eef0f5;
    --label-glow: rgba(44, 71, 132, 0.75);
  }
  * { margin: 0; padding: 0; box-sizing: border-box; }
  html, body { width: 1200px; height: 900px; overflow: hidden; }
  body {
    position: relative;
    font-family: "Open Sans", Arial, sans-serif;
    background: linear-gradient(to bottom, var(--page-top) 9%, var(--page-bottom) 100%);
  }
  .site-header {
    position: absolute; left: 0; top: 0; width: 1200px; height: 81px;
    background: var(--brand-blue);
    color: var(--white);
  }
  .site-title {
    position: absolute; left: 49px; top: 24px;
    font-size: 23px; font-weight: 400; letter-spacing: -0.2px;
  }
  .site-date {
    position: absolute; right: 66px; top: 30px;
    font-size: 17px; letter-spacing: 4px;
  }
  .survey-card {
    position: absolute; left: 279px; top: 141px; width: 651px; height: 403px;
    background: var(--brand-blue);
    border-radius: 20px;
    padding: 13px;
    box-shadow: 0 6px 14px rgba(0,0,0,0.35);
  }
  .survey-card__inner {
    position: relative; width: 100%; height: 100%;
    background: var(--panel-fill);
    border: 2px solid var(--panel-edge);
    border-radius: 10px;
  }
  .survey-card__headline {
    position: absolute; left: 0; right: 0; top: 22px;
    text-align: center;
    font-size: 33px; font-weight: 300; color: var(--white);
    text-shadow: 0 0 3px rgba(60,80,130,0.45);
  }
  .survey-card__text {
    position: absolute; left: 28px; top: 90px;
    font-size: 13.5px; font-weight: 600; line-height: 16.6px;
    letter-spacing: 1.6px; color: var(--text-blue);
    white-space: nowrap;
  }
  .cta {
    position: absolute; left: 0; right: 0; top: 222px;
    display: flex; flex-direction: column; align-items: center;
    text-decoration: none;
  }
  .cta__icon { width: 86px; height: 86px; display: block; }
  .cta__label {
    margin-top: 2px;
    font-size: 19px; line-height: 26px; font-weight: 400; color: var(--white);
    text-shadow: 0 0 3px var(--label-glow), 0 1px 2px var(--label-glow);
  }
  .site-footer {
    position: absolute; left: 0; right: 0; top: 852px;
    text-align: center; font-size: 18px; color: var(--footer-text);
  }
</style>
</head>
<body>
  <header class="site-header">
    <div class="site-title">Social Network Umfrage</div>
    <div class="site-date">Jul 02, 2011</div>
  </header>

  <main class="survey-card">
    <div class="survey-card__inner">
      <h1 class="survey-card__headline">Herzlichen Glückwunsch!</h1>
      <p class="survey-card__text">
        Sie wurden als einer von wenigen Nutzern aus Berlin und<br>
        Umgebung ausgewählt an unserer Umfrage über Social<br>
        Networks teilzunehmen. Die Beantwortung der Fragen dauert<br>
        nur wenige Sekunden. Als Dankeschön für Ihre Teilnahme<br>
        können Sie ein Zelvo4, Trenu2 oder Pelwin Slate gewinnen.
      </p>
      <a class="cta" href="#">
        <svg class="cta__icon" viewBox="0 0 88 88" aria-hidden="true">
          <defs>
            <radialGradient id="ctaFill" cx="40%" cy="30%" r="75%">
              <stop offset="0%" stop-color="#5d7fc4"/>
              <stop offset="100%" stop-color="#2a4684"/>
            </radialGradient>
          </defs>
          <circle cx="44" cy="44" r="42" fill="url(#ctaFill)" stroke="#e6e9f0" stroke-width="2"/>
          <path d="M20 46 L34 40 L42 56 L66 14 L74 20 L44 70 L36 70 Z" fill="#ffffff" stroke="#c9d2e4" stroke-width="1.5" stroke-linejoin="round"/>
        </svg>
        <span class="cta__label">Jetzt teilnehmen</span>
      </a>
    </div>
  </main>

  <footer class="site-footer">2011 All Rights Reserved</footer>
</body>
</html>
```